CEDAR PEAK HEATING AND COOLING

Industry/Entity Type

Hvac

Requirements
Must have
• logo
My name: Tom Brennerov
Phone number 905-334-6071
Text:
Furnace and AC repairs
New furnace and AC installation
Ductwork
Gas lines
Water Tanks
Tankless water heaters
Nice to have
• Profesional modern look

```html
<!DOCTYPE html>
<html lang="en">
<head>
<meta charset="utf-8">
<title>Cedar Peak Heating and Cooling – Business Card</title>
<link href="https://fonts.googleapis.com/css2?family=Cinzel:wght@500;600&family=Montserrat:wght@400;500;600&display=swap" rel="stylesheet">
<style>
  :root {
    --backdrop: #1b1b1d;
    --card-white: #ffffff;
    --card-dark: #2e2e30;
    --brand-blue: #1553a5;
    --brand-green: #7bbd42;
    --text-white: #ffffff;
    --text-light: #e9e9e9;
  }
  * { margin: 0; padding: 0; box-sizing: border-box; }
  html, body {
    width: 1200px; height: 786px; overflow: hidden;
    background: var(--backdrop);
  }
  .canvas {
    position: relative; width: 1200px; height: 786px;
    display: flex; align-items: center; justify-content: center; gap: 40px;
  }
  .card {
    position: relative; width: 540px; height: 309px; overflow: hidden;
    border-radius: 3px;
    box-shadow: 0 18px 40px rgba(0,0,0,.55);
  }
  .card-front { background: var(--card-white); }
  .card-back { background: var(--card-dark); }

  .front-shapes { position: absolute; inset: 0; }

  .logo-square {
    width: 30px; height: 30px; flex: none;
    background: var(--brand-blue);
  }

  .front-brand {
    position: absolute; left: 110px; top: 58px;
    display: flex; align-items: center; gap: 12px;
  }
  .front-brand .brand-text {
    font-family: "Cinzel", serif; font-weight: 600;
    color: var(--brand-blue); text-align: center; line-height: 1.1;
  }
  .front-brand .brand-main { display: block; font-size: 26px; letter-spacing: 1px; }
  .front-brand .brand-sub { display: block; font-size: 9.5px; letter-spacing: 1.5px; margin-top: 4px; }

  .holder {
    position: absolute; right: 218px; top: 218px;
    color: var(--text-white); text-align: right; white-space: nowrap;
  }
  .holder-name { font-family: "Cinzel", serif; font-weight: 500; font-size: 20px; letter-spacing: .5px; }
  .holder-role { font-family: "Montserrat", sans-serif; font-size: 12px; margin-top: 2px; }

  .divider {
    position: absolute; left: 337px; top: 205px; width: 1px; height: 62px;
    background: var(--text-white);
  }

  .contact {
    position: absolute; left: 352px; top: 202px; list-style: none;
    font-family: "Montserrat", sans-serif; font-size: 11.5px;
    color: var(--text-white);
  }
  .contact li { display: flex; align-items: center; gap: 6px; line-height: 22px; }
  .contact svg { width: 10px; height: 10px; flex: none; }

  .back-brand {
    position: absolute; left: 0; right: 0; top: 80px;
    display: flex; align-items: center; justify-content: center; gap: 16px;
  }
  .back-brand .logo-square { width: 44px; height: 44px; }
  .back-brand .brand-text { text-align: center; }
  .back-brand .brand-main {
    display: block; font-family: "Cinzel", serif; font-weight: 600;
    font-size: 40px; letter-spacing: 1px; color: var(--brand-blue); line-height: 1.2;
  }
  .back-brand .brand-sub {
    display: flex; align-items: center; justify-content: center; gap: 10px;
    font-family: "Montserrat", sans-serif; font-weight: 600; font-size: 12px;
    letter-spacing: 1px; color: var(--text-light); margin-top: 2px;
  }
  .back-brand .brand-sub::before,
  .back-brand .brand-sub::after {
    content: ""; width: 44px; height: 1px; background: var(--text-light);
  }

  .services {
    position: absolute; left: 0; right: 0; top: 200px; text-align: center;
    font-family: "Montserrat", sans-serif; font-size: 12.5px;
    color: var(--text-light); line-height: 24px;
  }
  .services .sep { color: var(--brand-green); margin: 0 4px; }
</style>
</head>
<body>
<main class="canvas">

  <section class="card card-front" aria-label="Business card front">
    <svg class="front-shapes" viewBox="0 0 540 309" width="540" height="309" aria-hidden="true">
      <path d="M30 309 C 90 210, 260 140, 540 72 L540 309 Z" fill="var(--brand-blue)"/>
      <path d="M16 309 C 78 198, 250 126, 540 60 L540 68 C 256 132, 88 204, 26 309 Z" fill="var(--brand-green)"/>
    </svg>

    <div class="front-brand">
      <span class="logo-square" aria-hidden="true"></span>
      <div class="brand-text">
        <span class="brand-main">Cedar Peak</span>
        <span class="brand-sub">HEATING AND COOLING</span>
      </div>
    </div>

    <div class="holder">
      <div class="holder-name">TOM BRENNEROV</div>
      <div class="holder-role">Director</div>
    </div>

    <div class="divider"></div>

    <ul class="contact">
      <li>
        <svg viewBox="0 0 10 10" aria-hidden="true"><path d="M2 0.5 L3.6 2.6 L2.8 3.6 C3.4 5 4.8 6.4 6.4 7.2 L7.4 6.4 L9.5 8 L8.4 9.5 C4.5 9.2 0.8 5.5 0.5 1.6 Z" fill="currentColor"/></svg>
        905-334-6071
      </li>
      <li>
        <svg viewBox="0 0 10 10" aria-hidden="true"><rect x="0.7" y="2" width="8.6" height="6" fill="none" stroke="currentColor" stroke-width="1"/><path d="M0.7 2 L5 5.5 L9.3 2" fill="none" stroke="currentColor" stroke-width="1"/></svg>
        info@cedarpeakhvac.com
      </li>
      <li>
        <svg viewBox="0 0 10 10" aria-hidden="true"><circle cx="5" cy="5" r="4.3" fill="none" stroke="currentColor" stroke-width="1"/><ellipse cx="5" cy="5" rx="1.8" ry="4.3" fill="none" stroke="currentColor" stroke-width=".8"/><path d="M0.7 5 H9.3" stroke="currentColor" stroke-width=".8"/></svg>
        www.cedarpeakhvac.com
      </li>
    </ul>
  </section>

  <section class="card card-back" aria-label="Business card back">
    <div class="back-brand">
      <span class="logo-square" aria-hidden="true"></span>
      <div class="brand-text">
        <span class="brand-main">Cedar Peak</span>
        <span class="brand-sub">HEATING AND COOLING</span>
      </div>
    </div>
    <p class="services">
      Furnace and AC repairs<span class="sep">|</span>New furnace and AC installation<br>
      Ductwork<span class="sep">|</span>Gas lines<span class="sep">|</span>Water Tanks<span class="sep">|</span>Tankless water heaters
    </p>
  </section>

</main>
</body>
</html>
```